Oil and Gas Letterhead Design Tweak

Simple letterhead information and design tweak.

Please note, we don't want to change the design or logo of the letterhead only the small changes mentioned below.

We need to change the company name up top to "Northvale Petrotech Kestra"

Also, we need to include in the footer the following information. I have attached an image of roughly how we would like to have it displayed in the footer.

Footer Details:

Northvale Petrotech Kestra,
Unit No. 7283, Kestra Business Center, level No. 2, R&P 8, Dubai, United Arab Emirates
Northvale Petrotech Kestra is registered as a free zone company under the rules & regulations of Kestra

Target Market(s)

O&G Market

Industry/Entity Type

Oil And Gas

Font styles to use
Sans Serif

Colors

Designer to choose colors to be used in the design.

Requirements
Must have
• Change the company name to Northvale Petrotech Kestra
• Include the footer on the bottom of the first and continuation page
Should not have
• Should not change the design or logo of the letterhead, only the specified changes mentioned above

```html
<!DOCTYPE html>
<html lang="en">
<head>
<meta charset="utf-8">
<title>Northvale Petrotech Kestra — Letterhead</title>
<link href="https://fonts.googleapis.com/css2?family=Open+Sans:wght@400;600;700&display=swap" rel="stylesheet">
<style>
  :root {
    --brand-blue: #1455a6;
    --brand-red: #e8202a;
    --ink: #2b2b2b;
    --ink-soft: #3a3a3a;
    --rule: #b9b9b9;
    --paper: #ffffff;
  }
  html, body {
    margin: 0;
    padding: 0;
    width: 985px;
    height: 1200px;
    overflow: hidden;
    background: var(--paper);
  }
  .letterhead {
    position: relative;
    width: 985px;
    height: 1200px;
    background: var(--paper);
    font-family: "Open Sans", Arial, sans-serif;
  }
  .top-band-blue,
  .top-band-red {
    position: absolute;
    top: 0;
    height: 16px;
  }
  .top-band-blue {
    left: 0;
    width: 88px;
    background: var(--brand-blue);
  }
  .top-band-red {
    left: 160px;
    right: 0;
    background: var(--brand-red);
  }
  .masthead {
    position: absolute;
    top: 54px;
    left: 150px;
    display: flex;
    align-items: center;
    gap: 14px;
  }
  .masthead-mark {
    width: 22px;
    height: 22px;
    background: var(--brand-red);
  }
  .company-name {
    margin: 0;
    font-size: 27px;
    font-weight: 600;
    color: var(--ink);
    text-transform: uppercase;
  }
  .footer {
    position: absolute;
    left: 65px;
    top: 1110px;
    width: 700px;
  }
  .footer-name {
    margin: 0 0 7px;
    font-size: 15px;
    font-weight: 700;
    color: var(--brand-blue);
    text-transform: uppercase;
  }
  .footer-rule {
    width: 588px;
    border-top: 1px solid var(--rule);
    margin: 0 0 8px;
  }
  .footer-line {
    margin: 0 0 6px;
    font-size: 13px;
    color: var(--ink-soft);
    white-space: nowrap;
  }
  .corner-tab {
    position: absolute;
    bottom: 0;
    width: 44px;
    height: 14px;
  }
  .corner-tab.blue { left: 782px; background: var(--brand-blue); }
  .corner-tab.red { left: 830px; background: var(--brand-red); }
</style>
</head>
<body>
  <main class="letterhead">
    <div class="top-band-blue" aria-hidden="true"></div>
    <div class="top-band-red" aria-hidden="true"></div>

    <header class="masthead">
      <span class="masthead-mark" aria-hidden="true"></span>
      <h1 class="company-name">Northvale Petrotech Kestra</h1>
    </header>

    <footer class="footer">
      <p class="footer-name">Northvale Petrotech Kestra,</p>
      <div class="footer-rule"></div>
      <p class="footer-line">Unit No. 7283, Kestra Business Center, level No. 2, R&amp;P 8, Dubai, United Arab Emirates</p>
      <p class="footer-line">Northvale Petrotech Kestra is registered as a free zone company under the rules &amp; regulations of Kestra</p>
    </footer>

    <div class="corner-tab blue" aria-hidden="true"></div>
    <div class="corner-tab red" aria-hidden="true"></div>
  </main>
</body>
</html>
```